Silver Brook Decorators Banner

Create a banner that displays and reinforces Silver Brook Decorators’ brand identity while promoting our interior painting services. The banner will be displayed at indoor venues through the winter. The design should be clean, professional, and visually recognizable to both new and returning customers. See attached design brief & logo source files.

```html
<!DOCTYPE html>
<html lang="en">
<head>
<meta charset="utf-8">
<title>Silver Brook Decorators Banner</title>
<link rel="stylesheet" href="https://fonts.googleapis.com/css2?family=Bebas+Neue&family=Montserrat:wght@500;700;800&display=swap">
<style>
  :root {
    --green: #6b8f4e;
    --ink: #1b1b1b;
    --white: #ffffff;
    --backdrop: #dedede;
    --photo-warm: #a07a52;
    --photo-cool: #8a9aa6;
  }
  * { margin: 0; padding: 0; box-sizing: border-box; }
  html, body { width: 1111px; height: 1200px; overflow: hidden; }
  body { background: var(--backdrop); position: relative; font-family: "Montserrat", sans-serif; }

  .banner {
    position: absolute; left: 30px; top: 390px;
    width: 1050px; height: 420px;
    background: var(--white); overflow: hidden;
  }
  .headline {
    position: absolute; left: 32px; top: 18px;
    font-family: "Bebas Neue", sans-serif;
    font-size: 146px; line-height: 1; color: var(--ink);
    letter-spacing: -1px; white-space: nowrap;
  }
  .brand {
    position: absolute; left: 796px; top: 20px; width: 220px;
    text-align: center; color: var(--green); font-weight: 800; line-height: 1.05;
  }
  .brand-dot {
    width: 54px; height: 54px; border-radius: 50%;
    background: var(--green); margin: 0 auto 10px;
  }
  .brand-line1 { font-size: 25px; letter-spacing: 0.5px; }
  .brand-line2 { font-size: 31px; }

  .services-frame { position: absolute; left: 0; top: 0; }
  .services-title {
    position: absolute; left: 50px; top: 156px;
    font-size: 23px; font-weight: 500; color: var(--ink); letter-spacing: 0.3px;
  }
  .service {
    position: absolute; height: 30px;
    background: var(--ink); border-radius: 15px;
    color: var(--white); font-weight: 800; font-size: 17px;
    display: flex; align-items: center; padding-left: 30px;
  }
  .service .icon {
    position: absolute; left: -20px; top: -6px;
    width: 42px; height: 42px; border-radius: 50%;
    background: var(--green); border: 2px solid var(--white);
  }
  .service .icon svg { width: 100%; height: 100%; }
  .service.two-line { font-size: 15px; line-height: 0.9; height: 36px; border-radius: 18px; }
  .service.two-line .icon { top: -3px; }

  .photo {
    position: absolute; border-radius: 50%;
    border: 6px solid var(--green);
  }
  .photo-dining { left: 373px; top: 200px; width: 128px; height: 128px;
    background: radial-gradient(circle at 50% 45%, #d9c3a2, var(--photo-warm) 60%, #5b4530); }
  .photo-stair { left: 490px; top: 183px; width: 150px; height: 150px;
    background: radial-gradient(circle at 55% 40%, #e6e8ea, var(--photo-cool) 55%, #7b4a2a); }

  .cta {
    position: absolute; left: 37px; top: 376px; width: 250px;
    border-top: 2px solid var(--ink); border-bottom: 2px solid var(--ink);
    padding: 3px 0; font-size: 17px; font-weight: 800; color: var(--green); white-space: nowrap;
  }
  .cta strong { color: var(--ink); }
  .url {
    position: absolute; left: 300px; top: 370px;
    font-family: "Bebas Neue", sans-serif; font-size: 37px; line-height: 1;
    color: var(--ink); white-space: nowrap;
  }
  .url span { color: var(--green); }

  .swatch-art { position: absolute; left: 630px; top: 168px; }
</style>
</head>
<body>
  <section class="banner">
    <h1 class="headline">PAINT SMARTER!</h1>

    <div class="brand">
      <div class="brand-dot"></div>
      <div class="brand-line1">SILVER BROOK</div>
      <div class="brand-line2">DECORATORS</div>
    </div>

    <svg class="services-frame" width="1050" height="420" aria-hidden="true">
      <path d="M470 168 H602 Q621 168 621 187 V335 Q621 354 602 354 H48 Q29 354 29 335 V192 Q29 178 42 170"
            fill="none" stroke="var(--green)" stroke-width="2"/>
    </svg>
    <h2 class="services-title">INTERIOR PAINTING SERVICES:</h2>

    <div class="service" style="left:60px; top:202px; width:123px;">
      <span class="icon"><svg viewBox="0 0 42 42"><rect x="12" y="11" width="16" height="8" fill="#fff"/><rect x="19" y="19" width="3" height="13" fill="#fff"/></svg></span>WALLS</div>
    <div class="service" style="left:60px; top:250px; width:123px;">
      <span class="icon"><svg viewBox="0 0 42 42"><rect x="15" y="9" width="12" height="24" fill="none" stroke="#fff" stroke-width="2.5"/></svg></span>TRIM</div>
    <div class="service" style="left:60px; top:298px; width:131px;">
      <span class="icon"><svg viewBox="0 0 42 42"><rect x="10" y="12" width="22" height="18" fill="none" stroke="#fff" stroke-width="2.5"/><line x1="21" y1="12" x2="21" y2="30" stroke="#fff" stroke-width="2.5"/></svg></span>CABINETS</div>

    <div class="service" style="left:217px; top:202px; width:136px;">
      <span class="icon"><svg viewBox="0 0 42 42"><line x1="21" y1="8" x2="21" y2="18" stroke="#fff" stroke-width="2.5"/><path d="M12 26 L21 18 L30 26 Z" fill="#fff"/></svg></span>CEILINGS</div>
    <div class="service two-line" style="left:217px; top:247px; width:136px;">
      <span class="icon"><svg viewBox="0 0 42 42"><path d="M13 30 L22 10 L30 16 L22 32 Z" fill="#fff"/></svg></span>DRYWALL<br>REPAIR</div>
    <div class="service" style="left:222px; top:298px; width:124px;">
      <span class="icon"><svg viewBox="0 0 42 42"><rect x="13" y="9" width="16" height="24" fill="none" stroke="#fff" stroke-width="2"/><path d="M13 9 L29 21 M29 9 L13 21 M13 21 L29 33 M29 21 L13 33" stroke="#fff" stroke-width="1.5"/></svg></span>ACCESS</div>

    <div class="photo photo-dining" role="img" aria-label="Photo of a finished dining room with a long table and large windows"></div>
    <div class="photo photo-stair" role="img" aria-label="Photo of a bright hallway with a curved wooden spiral staircase"></div>

    <p class="cta">Book a <strong>Free Estimate</strong> at</p>
    <p class="url">WWW.<span>SILVERBROOKDECO</span>.COM</p>

    <svg class="swatch-art" width="420" height="252" role="img" aria-label="Fanned paint swatch cards in shades of green with a paintbrush resting on top">
      <defs>
        <linearGradient id="swatchFade" x1="0" y1="1" x2="1" y2="0">
          <stop offset="0" stop-color="#3f9a48"/>
          <stop offset="0.5" stop-color="#8fcf9c"/>
          <stop offset="1" stop-color="#dfe79a"/>
        </linearGradient>
      </defs>
      <path d="M40 252 Q75 150 140 60 L310 0 L420 40 L420 252 Z" fill="url(#swatchFade)"/>
    </svg>
  </section>
</body>
</html>
```